Scent Marketing Solutions by Vapolinth

We need to create 12 page brochure (including the cover and back page) for our Scent Marketing line of products.

The brochure size is 18 cm x 18 cm.

Our competitors are www.breeze-olfa.example and www.nosquell.example
Updates

Hi Designers, 

The budget for this project has been increased to $300. This is a 12 page brochure of size 18cm x 18cm.

Thank you.

Hi all designers,

I uploaded a new brochure draft with the write up in pdf.
I understand that some of you could not open the original file in powerpoint.

Thank you.

Hi Designers,

I added the brochure write up in Word and PDF format. I understand some of you have troubles with it in the earlier files uploaded.

Thank you.

Target Market(s)

B2B audience, such as visual merchandisers of retail brands, hotel managers, real estate property managers etc.

Industry/Entity Type

Marketing

Requirements
Must have
• Our corporate identity uses a lot of white, hence this must be reflected in the brochure.
Our products are high-tech and environmentally friendly, so this must again be reflected in the design.
We want to make the brochure attractive and easy to read, hence would like to allocate more space for photos and pictures and keep the brochure as spacious as possible.
Nice to have
• Since the product is related to the air (it scents the air), we would like to have a design feature that reflects this and is repeated throughout the brochure. It can be a pattern or logo.
Should not have
• Avoid using a lot of bright colors

```html
<!DOCTYPE html>
<html lang="en">
<head>
<meta charset="utf-8">
<title>Vapolinth – Scent Marketing Services</title>
<link rel="stylesheet" href="https://fonts.googleapis.com/css2?family=Tenor+Sans&family=Hind:wght@400;600&display=swap">
<style>
  :root {
    --paper: #ffffff;
    --heading-grey: #8a8a8a;
    --ink: #1e1e1e;
    --star: #555555;
    --photo-light: #f4f4f4;
    --photo-mid: #dcdcdc;
    --photo-warm: #e9d9a8;
    --air-soft: #e8edf5;
    --air-faint: #f4f6fa;
  }
  * { margin: 0; padding: 0; box-sizing: border-box; }
  html, body { width: 1200px; height: 600px; overflow: hidden; background: var(--paper); }
  .spread { position: relative; width: 1200px; height: 600px; background: var(--paper); font-family: "Hind", sans-serif; color: var(--ink); }
  .product-photo {
    position: absolute; left: 50px; top: 50px; width: 500px; height: 500px;
    background:
      radial-gradient(ellipse at 70% 45%, var(--photo-warm) 0%, rgba(233,217,168,0) 45%),
      linear-gradient(160deg, var(--photo-light) 0%, #ececec 55%, var(--photo-mid) 100%);
  }
  .air-texture {
    position: absolute; left: 550px; top: 330px; width: 650px; height: 270px;
    background:
      radial-gradient(ellipse 70% 60% at 65% 55%, var(--air-soft) 0%, var(--air-faint) 45%, rgba(255,255,255,0) 100%);
  }
  .services {
    position: absolute; left: 600px; top: 44px; width: 600px; text-align: center; z-index: 1;
  }
  .services-title {
    font-family: "Tenor Sans", sans-serif; font-weight: 400; color: var(--heading-grey);
    font-size: 30px; line-height: 48px; letter-spacing: 0; text-transform: uppercase;
  }
  .services-intro { margin-top: 12px; font-size: 11.5px; line-height: 19px; padding: 0 70px; }
  .services-list { list-style: none; margin-top: 6px; font-size: 11.5px; font-weight: 600; line-height: 23px; }
  .services-list li::before { content: "\2605"; color: var(--star); margin-right: 4px; }
  .services-cta { margin-top: 25px; font-size: 11.5px; line-height: 19px; }
  .services-contact { margin-top: 36px; font-size: 11.5px; line-height: 19px; }
  .services-contact strong { font-weight: 600; }
</style>
</head>
<body>
<main class="spread">
  <div class="product-photo" role="img" aria-label="Photograph of small glass vials of amber and clear fragrance oils with white caps and a roller bottle on a white surface"></div>

  <div class="air-texture" role="img" aria-label="Soft pale blue airy flowing texture"></div>

  <section class="services">
    <h1 class="services-title">Support all your scent<br>marketing needs</h1>
    <p class="services-intro">We make it easy and effortless to implement scent marketing into your business by providing a comprehensive range of services that include:</p>
    <ul class="services-list">
      <li>Signature scent design</li>
      <li>Scent selection</li>
      <li>Scent matching</li>
      <li>Application services</li>
      <li>Product development &amp; contract manufacturing</li>
    </ul>
    <p class="services-cta">Ready to unleash the power of scent marketing for your business?</p>
    <p class="services-contact">Email <strong>sales@vapolinth.example</strong>,<br>or visit <strong>www.vapolinth.example</strong> today to schedule your consultation.</p>
  </section>
</main>
</body>
</html>
```